VELRO - Business cards

Business card to be created for Commercial sales staff

Target Market(s)

Commercial businesses

Industry/Entity Type

Commercial

Contact Information for Business Card

Look professional. For commercial clients

Colors
ffffff

Requirements
Must have
• - Velro Logo
• - Commercial sales staff as postion
• - room for commerical sales manager role
• - person name and their mobile number
• - Website : velropower.com.au
Nice to have
• White background.
• On back of business card just have the logo no other information
Should not have
• Should only have white background on front of card.

```html
<!DOCTYPE html>
<html lang="en">
<head>
<meta charset="utf-8">
<title>VELRO – Business Cards</title>
<link rel="stylesheet" href="https://fonts.googleapis.com/css2?family=Roboto:wght@400;500;900&display=swap">
<style>
  :root {
    --backdrop: #d9d9d9;
    --card-front: #ffffff;
    --card-back-start: #1f1f1f;
    --card-back-end: #333333;
    --ink-dark: #2e3138;
    --ink-light: #ffffff;
    --accent-red: #d3222a;
  }
  * { box-sizing: border-box; margin: 0; padding: 0; }
  html, body {
    width: 1200px;
    height: 1000px;
    overflow: hidden;
    background: var(--backdrop);
    font-family: "Roboto", Arial, sans-serif;
  }
  .sheet {
    position: relative;
    width: 1200px;
    height: 1000px;
  }
  .card {
    position: absolute;
    left: 220px;
    width: 760px;
    border-radius: 28px;
    overflow: hidden;
    box-shadow: 0 6px 18px rgba(0,0,0,0.25);
  }
  .card--front {
    top: 50px;
    height: 432px;
    background: var(--card-front);
    display: flex;
    align-items: center;
    justify-content: center;
  }
  .card--back {
    top: 522px;
    height: 438px;
    background: linear-gradient(120deg, var(--card-back-start) 0%, var(--card-back-start) 45%, var(--card-back-end) 70%, var(--card-back-start) 100%);
  }
  .brand {
    display: flex;
    align-items: center;
    gap: 18px;
    font-weight: 900;
    letter-spacing: 2px;
    line-height: 1;
  }
  .brand__dot {
    border-radius: 50%;
    background: var(--accent-red);
    flex: none;
  }
  .card--front .brand { color: var(--ink-dark); font-size: 120px; }
  .card--front .brand__dot { width: 46px; height: 46px; }
  .card--back .brand {
    position: absolute;
    left: 378px;
    top: 78px;
    color: var(--ink-light);
    font-size: 76px;
    gap: 12px;
  }
  .card--back .brand__dot { width: 30px; height: 30px; }
  .details {
    position: absolute;
    left: 404px;
    top: 210px;
    color: var(--ink-light);
  }
  .details__role {
    font-size: 17px;
    font-weight: 400;
    line-height: 27px;
  }
  .details__name {
    margin-top: 30px;
    font-size: 22px;
    font-weight: 500;
    color: var(--accent-red);
  }
  .contact {
    list-style: none;
    margin-top: 14px;
  }
  .contact__item {
    display: flex;
    align-items: center;
    gap: 8px;
    font-size: 17px;
    line-height: 28px;
  }
  .contact__icon { width: 13px; height: 13px; flex: none; }
</style>
</head>
<body>
  <main class="sheet">
    <section class="card card--front" aria-label="Business card front">
      <div class="brand">
        <span class="brand__dot" aria-hidden="true"></span>
        <span class="brand__name">VELRO</span>
      </div>
    </section>

    <section class="card card--back" aria-label="Business card back">
      <div class="brand">
        <span class="brand__dot" aria-hidden="true"></span>
        <span class="brand__name">VELRO</span>
      </div>
      <div class="details">
        <p class="details__role">Commercial sales staff as postion</p>
        <p class="details__role">Commerical sales manager role</p>
        <p class="details__name">Daniel Hart</p>
        <ul class="contact">
          <li class="contact__item">
            <svg class="contact__icon" viewBox="0 0 13 13" aria-hidden="true">
              <rect x="3" y="0.5" width="7" height="12" rx="1.5" fill="none" stroke="#d3222a" stroke-width="1.3"/>
              <line x1="5.5" y1="10.3" x2="7.5" y2="10.3" stroke="#d3222a" stroke-width="1.2"/>
            </svg>
            <span>012-555-0142</span>
          </li>
          <li class="contact__item">
            <svg class="contact__icon" viewBox="0 0 13 13" aria-hidden="true">
              <circle cx="6.5" cy="6.5" r="5.6" fill="none" stroke="#d3222a" stroke-width="1.2"/>
              <ellipse cx="6.5" cy="6.5" rx="2.4" ry="5.6" fill="none" stroke="#d3222a" stroke-width="1"/>
              <line x1="0.9" y1="6.5" x2="12.1" y2="6.5" stroke="#d3222a" stroke-width="1"/>
            </svg>
            <span>velropower.com.au</span>
          </li>
        </ul>
      </div>
    </section>
  </main>
</body>
</html>
```